Our business name is Tremlow Skyworks Pty Ltd and we already have a logo. We would like the same colours that appear in our logo on our marketing material. I have attached our logo for colour consistency. We need a brochure designed that promotes our aerial photography and aerial imaging services. We'd like to use the brochure for electronic marketing purposes in an effort to attract a new client base. We are a new start up business so funds are fairly scarce. We use sophisticated UAV (unmanned aerial vehicle) or RPA - remotely piloted aircraft technology) that captures beautiful video and still images.
Our services are suitable for many types of industries and applications. We have identified at least 10 market sectors ranging, infrastructure inspections such as: gas pipelines, chemical and petrol storage facilities, pipeline and power line inspections, Archeological and geological surveys, vegetation mapping, wildlife surveys, agriculture and horticulture surveys, high end real estate, sport and event marketing. Our plan is to create a series of brochures (1) for each industry to help us market our business.

Our first brochure will focus on environmental management and compliance. We will target other industries down the track. These industries would see our service as helping them meet their compliance and auditing requirements.
We have a brochure that we put together containing words and some (very boring) format. As this will be one of a series of brochures, we'd like to colour code the industries for easy identification. (perhaps a green tab) in the corner to distinguish between our brochures. We have attached our boring brochure as a starting point. If we like the design there will be more work to follow. We want to be able to standardise the format for the other industries we will target. We anticipate needing another 6-8 brochures over the course of the next 2 months.
Updates

I have received questions regarding brochure size.  Apologies, I should have indicated in my posting previously.  The brochure is A3 landscape size so it can be folded in half to make 4 A4 pages.  We need to keep printing costs down so the content needs to be  within 4 pages.  I'm about to make some minor changes to the content to try to reduce the amount of text cause I can see this may be a problem.  Look forward to receiving your design. Thanking you in advance for your great work!

Re: Brochure Tremlow Environmental Compliance and Monitoring Services

I have reduced the amount of text contained in the original version of the brochure making it more succinct and less wordy.  Could you use the least amount of space because we want to be able to use this brochure as both electric marketing and print based.  I have also included additional photos which will give you more to work with.  Thank you for your work in advance!  Regards Marisa 

PLEASE NOTE - TEXT HAS BEEN UPDATED (REDUCED TEXT IN BROCHURE). COULD YOU REFER TO VERSION 2 OF TREMLOW ENVIRONMENTAL COMPLIANCE AND MONITORING SERVICES BROCHURE UPDATED FRIDAY 17TH.

Thanks Marisa 

Hi talented designers working on the Tremlow Brochure for Environmental Compliance and Monitoring.  I have been asked to upload the EPS version of Tremlow Logo.  I have just done so.

Regards
Marisa 

Hi all, to assist you with the design concept. I feel I need to clarity a number of points.  We are a new technology driven business.  No one else is conducting environmental surveys using this type of sophisticated equipment. We are in the business of providing clients with visual data (aerial images). Could you include grab lines in the brochure that draws attention to this. We us state of the art technology to produce high quality images efficiently, safely and economically. 

Thank you
Marisa

Reason: We need additional time to receive and review designs.

Reason: Need additional time to communicate with designers and to review changes. Thank you Marisa

I have extended the project date a few days. I have been incredibly impressed by the quality of your work and thank you all for your efforts.  I am waiting on a few revisions by a number of designers and look forward to receiving these changes.  We are close to completion.  Thanking you all again. Marisa 

Target Market(s)

We are targeting a wide range of industry sectors. Specifically, looking at targeting large engineering type consultancies, corporations, government agencies, auditing bodies. Typically, targeting the professional sector who use data to confirm, monitor and make better decisions.

We want the brochure design to be contemporary and modern which reflects what our business does. We use state of the art unmanned aerial technology to capture brilliant visual images and video. So we want our brochure to reflect that we're leaders in the field offering something different - cutting edge approach. I have additional photos that show vegetation mapping, wildlife surveys, agriculture and horticulture applications. Our services would benefit any business that uses visual data to help them make better, more informed decisions.

Industry/Entity Type

Business

Font styles to use
Serif
Sans Serif

Requirements
Must have
• We would like you to include photo of the UAV equipment/technology shots. This is new technology so we must also educate our clients on what our technology is capable of doing. We are offering a service that is very different so we want to be able to convey the true benefits of our services such as safety, efficiency, cost saving, reliability. We would like to convey these key themes. Credible data enables businesses to make better, faster decisions.
Nice to have
• We are essentially providing visual data in the form of high definition photos and videos. For this particular sector, data could be used for compliance or auditing purposes, planning, measuring, monitoring, evaluating, assessing, marketing. Could you please include these words in the brochure as they capture our service provision. Please note the red photo is infrared images.

```html
<!DOCTYPE html>
<html lang="en">
<head>
<meta charset="utf-8">
<title>Tremlow Skyworks – Brochure Cover Spread</title>
<link href="https://fonts.googleapis.com/css2?family=Jost:wght@300;400;500&display=swap" rel="stylesheet">
<style>
  :root {
    --brand-blue: #25aae2;
    --silver-light: #f4f4f4;
    --silver-mid: #d9d9d9;
    --silver-dark: #bdbdbd;
    --ink: #3a3a3a;
    --white: #ffffff;
    --backdrop: #ececec;
    --grass-light: #8cc04a;
    --grass-dark: #4f7a2c;
    --fold: #2b2b2b;
  }
  * { box-sizing: border-box; margin: 0; padding: 0; }
  html, body {
    width: 1200px; height: 886px; overflow: hidden;
    background: var(--backdrop);
    font-family: "Jost", sans-serif;
  }
  .spread {
    position: absolute; left: 20px; top: 33px;
    width: 1160px; height: 819px;
    display: flex;
    box-shadow: 0 6px 18px rgba(0,0,0,.25);
  }
  .page { position: relative; height: 100%; overflow: hidden; }
  .page--back { width: 581px; background: var(--brand-blue); border-right: 1px solid var(--fold); }
  .page--front { width: 579px; background: var(--brand-blue); }

  .silver-band {
    position: absolute; left: 0; right: 0;
    background: linear-gradient(90deg, var(--silver-dark) 0%, var(--silver-light) 45%, var(--silver-mid) 80%, var(--silver-dark) 100%);
  }
  .rule { position: absolute; left: 0; right: 0; height: 4px; background: var(--brand-blue); }
  .rule--white { height: 2px; background: var(--white); }

  /* Back page */
  .back-band { top: 216px; height: 262px; }
  .bio {
    position: absolute; left: 52px; top: 23px; width: 484px;
    font-size: 15px; font-weight: 300; line-height: 19.8px;
    color: var(--ink); text-align: justify; text-indent: 50px;
  }
  .back-footer { position: absolute; left: 0; right: 0; top: 596px; text-align: center; color: var(--white); }
  .wordmark { font-weight: 500; letter-spacing: -0.5px; line-height: 1; }
  .wordmark--back { font-size: 40px; color: var(--white); }
  .web { margin-top: 22px; font-size: 22px; font-weight: 300; letter-spacing: 1px; }
  .back-strip { position: absolute; left: 0; right: 0; bottom: 0; height: 19px;
    background: linear-gradient(90deg, var(--silver-dark), var(--silver-light) 50%, var(--silver-dark)); }

  /* Front page */
  .photo {
    position: absolute; left: 0; right: 0;
    background: linear-gradient(120deg, var(--grass-light) 0%, #7bb23f 45%, var(--grass-dark) 100%);
  }
  .photo--top { top: 0; height: 289px; }
  .photo--bottom { top: 404px; height: 397px; }
  .front-band { top: 293px; height: 106px; display: flex; align-items: center; justify-content: center; }
  .wordmark--front { font-size: 56px; color: var(--brand-blue); }
</style>
</head>
<body>
  <div class="spread">
    <section class="page page--back">
      <div class="rule rule--white" style="top:208px"></div>
      <div class="rule" style="top:211px"></div>
      <div class="silver-band back-band">
        <p class="bio">Marisa Vardell is Tremlow’s Business Development Manager. Marisa has spent a considerable part of her career in the corporate sector where she worked for leading global companies such as Aeroline Pacific, Kestrel Motors and Harrow Defence. She has held management roles in human resources, industrial relations and organisational development. Marisa has a strong focus on project management /client relations, OH&amp;S, audits, compliance and quality management systems. She is one of few people in Australia to be accredited by Kestrel Motor Corporation (Japan) as a Total Quality Management Facilitator &amp; Assessor. Marisa has spent a considerable part of her career supporting Engineering and Maintenance functions.</p>
      </div>
      <div class="rule" style="top:478px"></div>
      <div class="rule rule--white" style="top:482px"></div>
      <div class="back-footer">
        <div class="wordmark wordmark--back">TREMLOW</div>
        <div class="web">www.tremlow.com.au</div>
      </div>
      <div class="back-strip"></div>
    </section>

    <section class="page page--front">
      <div class="photo photo--top" role="img" aria-label="Aerial photograph of parkland with grass, trees and a winding red cycle path"></div>
      <div class="rule" style="top:289px"></div>
      <div class="silver-band front-band">
        <div class="wordmark wordmark--front">TREMLOW</div>
      </div>
      <div class="rule" style="top:399px"></div>
      <div class="photo photo--bottom" role="img" aria-label="Aerial photograph continuing the parkland, footpath and cycle path among trees"></div>
    </section>
  </div>
</body>
</html>
```